Tom & Nia's Homepage Design - Florists

Hello ArtHivePro,

We’re Tom and Nia and we own a lovely flower shop in Marlow. We’re looking to launch a website that gives our customers all information they need to know about getting in contact with us. In time we hope the website will grow and we will want to add new pages as we go along including ecommerce functionality, so the design will need to allow for this.

The brief:
We are looking for 1 homepage design. We have already had our logo designed, which we’ve attached for you to use. At the moment we’re keen to have a homepage design that showcases six of our most popular bouquets, see attached pictures and our contact details. We are looking for a contemporary design that’s inline with our logo. Please do not use dark background colours, we want a clean, light and simple design that looks fresh, modern and professional. Please remember that the majority of web monitors now use a screen resolution of 1366x768. Therefore please do not design a 800 x 600 homepage.

1. Our logo and icon (See attachments)
2. Potential hero images attached for inspiration. 6 Bouquets attached but dont make it look like a bog standard ecommerce site. You dont have to use the 6 bouquets. Our site is more brand as we dont have ecom functionality yet.
3. Our contact details including:

Name:
Tom and Nia’s (note 1 ‘L’ in Nia’s name, use the logo)

Navigation

Homepage needs to include the following copy
‘Free delivery with all orders”
‘Fresh – 7 days of flower freshness guaranteed’
‘Hand delivered and hand prepared by a professional florist’
Very clear call to action to ‘Order today: 0203 574 2261 or email us (visually a clickable link) today

Payment visuals: show that we accept KORVA/Paymoriant/Harbour Quickcard/Zentrip, with logos

Telephone numbers:
0203 574 2261 (Central London)
0208 417 5309 (Greater London)
01628 735142 (Marlow)
07812 906218 (Mobile)

E-mail address
orders@tomandnias.co.uk (Orders)
CS@tomandnias.co.uk (Customer Service)

Chatterly page link (use CH logo)
http://www.facebook.com/tomandnias

The Northfield Petal Guild logo
Attached should be displayed on the bottom of the homepage somewhere, prefer bottom right.

Other sites we like:
http://www.bloomsbygwendra.com
http://maisonvertilune.com
Like the fun of this one - http://www.puddlegoose.co.uk/goto/home

Our logo should be a good guide for how we’d like the overall page to look, please use this as a starter for your designs. Fee; free to submit your designs and I’ll feedback on changes.

We look forward to seeing your designs!

Tom & Nia

Industry/Entity Type

Florist

Requirements
Must have
• Please see the attached brief. Please use our logo and icon in the design.
Should not have
• Do not use dark background colours, it should feel light and fresh.

```html
<!DOCTYPE html>
<html lang="en">
<head>
<meta charset="utf-8">
<title>Tom &amp; Nia's – Florists</title>
<link href="https://fonts.googleapis.com/css2?family=Questrial&family=Quicksand:wght@400&family=Sorts+Mill+Goudy&family=Ubuntu:wght@400;500;700&family=Roboto:wght@400&family=Open+Sans:wght@400&display=swap" rel="stylesheet">
<style>
:root{
  --coral:#f26163;
  --coral-dark:#c84446;
  --purple:#9b4ca0;
  --ink:#4a4a4a;
  --muted:#666;
  --price:#e31e24;
  --promo-red:#e31b23;
  --promo-yellow:#ffe600;
  --cyan:#45bde6;
  --navy:#2b3a6b;
  --pink:#e84a8f;
  --leaf:#a8d67c;
  --white:#fff;
}
*{box-sizing:border-box;margin:0;padding:0}
html,body{width:1200px;height:1089px;overflow:hidden}
body{position:relative;font-family:"Open Sans",Arial,sans-serif;background:#f2f2f2}
.backdrop{position:absolute;inset:0 0 288px 0;background:radial-gradient(circle at 1110px 190px,#f6a9d2 0,#f1b7d6 90px,rgba(240,240,240,0) 230px),linear-gradient(90deg,#e9e9e9,#fafafa 30%,#fdfdfd 70%,#e3e3e3)}
.page{position:absolute;left:159px;top:0;width:883px;height:801px;background:var(--white)}
.header{position:absolute;left:0;top:0;width:1200px;height:108px}
.brand{position:absolute;left:160px;top:56px;display:flex;align-items:center;gap:8px;font-family:"Questrial",sans-serif;font-size:30px;line-height:1;color:var(--ink);letter-spacing:-1px;white-space:nowrap}
.brand-dot{width:12px;height:12px;border-radius:50%;background:var(--coral)}
.social{position:absolute;left:978px;top:7px;display:flex;gap:7px}
.social a{width:21px;height:21px;border-radius:3px;background:#3b66b0;color:#fff;font:500 9px/21px "Ubuntu",sans-serif;text-align:center;text-decoration:none}
.social a.chirp{background:#4cb7e3}
.order-line{position:absolute;right:169px;top:38px;font-family:"Sorts Mill Goudy",serif;font-size:23px;color:#888;letter-spacing:.5px;white-space:nowrap}
.order-line strong{font-weight:400;font-size:26px}
.nav{position:absolute;left:367px;top:80px;display:flex;font-family:"Quicksand",sans-serif;font-size:14.5px;color:#666;white-space:nowrap}
.nav a{color:inherit;text-decoration:none;padding:0 10px;border-left:1px solid #ccc;line-height:17px}
.nav a:last-child{padding-right:0}
.nav a:first-child{border:0;padding-left:0;color:var(--coral);position:relative}
.nav a:first-child::after{content:"";position:absolute;left:13px;top:20px;border:5px solid transparent;border-bottom-color:var(--coral)}
.rule{position:absolute;left:159px;top:105px;width:883px;height:3px;background:var(--coral)}
.hero{position:absolute;left:159px;top:108px;width:883px;height:299px;background:linear-gradient(90deg,#f6f4f3 0,#f1efee 38%,#ec6a3a 55%,#d8301f 72%,#f09a55 85%,#e9e3e0 100%)}
.hero-copy{position:absolute;left:194px;top:213px}
.hero-title{font:700 36px/1 "Ubuntu",sans-serif;color:var(--ink);letter-spacing:.5px}
.hero-title span{color:var(--coral)}
.hero-phone{margin-top:17px;font:700 43px/1 "Ubuntu",sans-serif;color:var(--purple);letter-spacing:1px}
.cta{position:absolute;left:187px;top:322px;width:252px;height:33px;border-radius:17px;background:linear-gradient(#e8656a,var(--coral-dark));color:#fff;font:500 16px/33px "Ubuntu",sans-serif;padding-left:17px;text-decoration:none}
.cta::after{content:"";position:absolute;right:16px;top:10px;width:13px;height:13px;border-radius:50%;background:#fff}
.cta::before{content:"";position:absolute;right:20px;top:13px;border:3.5px solid transparent;border-left:5px solid var(--coral-dark);z-index:1}
.dots{position:absolute;left:563px;top:382px;display:flex;gap:8px}
.dots i{width:15px;height:15px;border-radius:50%;background:#ddd}
.dots i:last-child{background:#f4f4f4}
.promo{position:absolute;top:416px;width:285px;height:120px;text-align:center}
.promo-delivery{left:166px;background:var(--promo-red);border:1px solid #c5141b}
.promo-delivery b{display:block;margin-top:28px;font:700 34px/1 "Ubuntu",sans-serif;color:var(--promo-yellow);letter-spacing:1px}
.promo-delivery span{display:block;margin-top:7px;font:400 24px/1 "Quicksand",sans-serif;color:#fff}
.promo-fresh{left:458px;background:#fafafa;border:1px solid #ccc;font-family:"Ubuntu",sans-serif}
.promo-fresh .l1{margin-top:10px;font:700 29px/1 "Ubuntu";color:var(--cyan)}
.promo-fresh .l2{margin-top:5px;font-size:26px;color:var(--ink)}
.promo-fresh .l2 b{color:var(--pink)}
.promo-fresh .l3{margin-top:5px;font:700 28px/1 "Ubuntu";color:var(--navy)}
.promo-florist{left:750px;background:#fff;border-top:6px solid var(--leaf);border-bottom:6px solid var(--leaf);font-family:"Ubuntu",sans-serif;text-align:left}
.promo-florist p{position:absolute;left:0;width:232px;text-align:center;font-size:18px;color:var(--cyan);z-index:1;white-space:nowrap}
.promo-florist .p1{top:19px}
.promo-florist .p2{top:45px;color:#6bb34a;font-size:17px}
.promo-florist .p3{top:73px;font-size:15.5px;font-weight:500;color:#f277b0;letter-spacing:.3px}
.promo-florist .bouquet{position:absolute;right:5px;top:4px;width:40px;height:98px;border-radius:40% 40% 20% 20%;background:linear-gradient(#f0667a,#f6a3a8 60%,#f2d2c8)}
.product{position:absolute;top:546px;width:157px}
.product .photo{height:182px}
.product h3{margin-top:6px;font:400 16.5px/1 "Roboto",sans-serif;color:#555}
.product p{margin-top:7px;font-size:12px;color:var(--muted)}
.product p b{font-weight:400;color:var(--price)}
.footer{position:absolute;left:0;top:801px;width:1200px;height:288px;background:var(--coral);border-top:3px solid #1a1a1a;color:#fff}
.footer h4{position:absolute;top:22px;font-weight:400;font-size:16px}
.links{position:absolute;left:167px;top:52px;width:193px;list-style:none}
.links li{height:27.7px;border-bottom:1px solid #f8a9aa;font-size:12px;line-height:29px;padding-left:14px;position:relative}
.links li::before{content:"";position:absolute;left:3px;top:13px;width:5px;height:5px;border-radius:50%;background:#f8b4b5}
.contact{position:absolute;left:446px;top:47px;font-size:12.5px;line-height:23px}
.contact ul{list-style:none;padding-left:24px;position:relative}
.contact svg{position:absolute;left:0;top:4px}
.contact .mail{margin-top:23px}
.form{position:absolute;left:775px;top:46px}
.form label{display:flex;align-items:center;gap:10px;font-size:12px;margin-bottom:11px}
.form .field{width:173px;height:23px;background:#fff;border:1px solid #ddd}
.form .message{width:260px;height:90px;background:#fff;border:1px solid #ddd}
.send{margin-top:13px;width:74px;height:28px;background:linear-gradient(#c9393c,#8e1e22);border:1px solid #e88;font:700 13px/26px "Ubuntu",sans-serif;color:#fff;text-align:center;letter-spacing:.5px}
.bottom-rule{position:absolute;left:0;top:257px;width:1200px;height:1px;background:#f69093}
.copyright{position:absolute;left:169px;top:266px;font-size:13.5px;font-family:Arial,sans-serif}
</style>
</head>
<body>
<div class="backdrop" role="img" aria-label="Soft grey backdrop with a large pink gerbera flower on the right"></div>
<div class="page"></div>

<header class="header">
  <div class="brand"><span class="brand-dot"></span>Tom &amp; Nia's</div>
  <nav class="social"><a href="#" aria-label="Chatterly">CH</a><a href="#" class="chirp" aria-label="Chirpwell">CW</a></nav>
  <div class="order-line">Order today: <strong>0203 574 2261</strong></div>
  <nav class="nav">
    <a href="#">home</a><a href="#">classic flowers</a><a href="#">luxury bouquets</a><a href="#">platinum collection</a><a href="#">autumn flowers</a><a href="#">luxury roses</a>
  </nav>
</header>
<div class="rule"></div>

<section class="hero" role="img" aria-label="Bouquet of red and orange roses on a white table"></section>
<div class="hero-copy">
  <div class="hero-title">ORDER <span>TODAY</span></div>
  <div class="hero-phone">0203 574 2261</div>
</div>
<a href="#" class="cta">Contact us and Order now</a>
<div class="dots"><i></i><i></i><i></i></div>

<div class="promo promo-delivery"><b>FREE DELIVERY</b><span>with all orders</span></div>
<div class="promo promo-fresh">
  <div class="l1">FRESH – 7 DAYS</div>
  <div class="l2">of <b>FLOWER</b> freshness</div>
  <div class="l3">GUARANTEED</div>
</div>
<div class="promo promo-florist">
  <div class="bouquet" role="img" aria-label="Small mixed bouquet"></div>
  <p class="p1">Hand delivered</p>
  <p class="p2">and hand prepared by a</p>
  <p class="p3">PROFESSIONAL FLORIST'</p>
</div>

<div class="product" style="left:167px"><div class="photo" role="img" aria-label="Autumn Love bouquet of calla lilies and roses" style="background:linear-gradient(#8a7a6a,#cdb8a6 60%,#7a5a3e)"></div><h3>Autumn Love</h3><p>Our price: <b>$24.99</b></p></div>
<div class="product" style="left:345px"><div class="photo" role="img" aria-label="Autumn Wonders arrangement of lilac roses on an old chair" style="background:linear-gradient(#4a4a44,#8a8a80 55%,#6d7a58)"></div><h3>Autumn Wonders</h3><p>Our price: <b>$27.99</b></p></div>
<div class="product" style="left:522px"><div class="photo" role="img" aria-label="Be My Sweet Heart heart-shaped floral wreath" style="background:linear-gradient(#e4e2dc,#7e8a5a 50%,#d9d6ce)"></div><h3>Be My Sweet Heart</h3><p>Our price: <b>$35.99</b></p></div>
<div class="product" style="left:701px"><div class="photo" role="img" aria-label="Pastel wedding flowers in a silver bowl" style="background:linear-gradient(#5c6a48,#e8d6d0 50%,#7a6248)"></div><h3>Wedding flowers</h3><p>Our price: <b>$24.99</b></p></div>
<div class="product" style="left:878px"><div class="photo" role="img" aria-label="Wedding bouquet of peach roses and lavender" style="background:linear-gradient(#6a7a58,#f0d6c8 55%,#7d7060)"></div><h3>Wedding</h3><p>Our price: <b>$20.99</b></p></div>

<footer class="footer">
  <h4 style="left:167px">Recommended links</h4>
  <ul class="links">
    <li>Latest Designs</li><li>Our Favourites</li><li>Delivery Information</li><li>Customer Service</li><li>FAQ</li><li>About Us</li>
  </ul>

  <h4 style="left:446px">Contact us</h4>
  <div class="contact">
    <ul>
      <svg width="13" height="13" viewBox="0 0 24 24"><path fill="#fbc4c5" d="M6.6 10.8a15 15 0 0 0 6.6 6.6l2.2-2.2c.3-.3.7-.4 1-.2 1.1.4 2.3.6 3.6.6.6 0 1 .4 1 1V20c0 .6-.4 1-1 1A17 17 0 0 1 3 4c0-.6.4-1 1-1h3.5c.6 0 1 .4 1 1 0 1.2.2 2.4.6 3.6.1.3 0 .7-.2 1z"/></svg>
      <li>0203 574 2261 (Central London)</li>
      <li>0208 417 5309 (Greater London)</li>
      <li>01628 735142 (Marlow)</li>
      <li>07812 906218 (Mobile)</li>
    </ul>
    <ul class="mail">
      <svg width="14" height="11" viewBox="0 0 14 11"><rect x=".5" y=".5" width="13" height="10" fill="none" stroke="#fbc4c5"/><path d="M.5 .5 7 6l6.5-5.5" fill="none" stroke="#fbc4c5"/></svg>
      <li>orders@tomandnias.co.uk&nbsp; (Orders)</li>
      <li>CS@tomandnias.co.uk (Customer Service)</li>
    </ul>
  </div>

  <h4 style="left:775px">Write us</h4>
  <div class="form">
    <label><span class="field"></span>Name*</label>
    <label><span class="field"></span>Email*</label>
    <div class="message"></div>
    <div class="send">SEND</div>
  </div>

  <div class="bottom-rule"></div>
  <div class="copyright">Copyright © 2012 Tomandnias.co.uk. All Rights Reserved</div>
</footer>
</body>
</html>
```